Hualuoya herb bottle label

we need a new label design to reflect our branding for our Chinese herbal medicine product bottles. We import herbs from China and distribute them to Australian Practitioners. The product may be visible to their clients so we want to present it well. Our branding colours and images are attached below, as is the current label layout template. The manufacturer adds the individual names of the herbs and other details over the top so the back ground must be subtle. We would like our name - HuaLuoya at the top to possibly be in yellow/gold and in our chosen font (it will need to be saved and inserted as an image as last print run it reverted to a default font). we would like the blue mountains of the picture below incorporated as the back ground colours. The design needs to feel traditional and artistic. Our name Hualuoya means - essence and spirit. We represent the essence and spirit of traditional Chinese herbal medicine.

```html
<!DOCTYPE html>
<html lang="en">
<head>
<meta charset="utf-8">
<title>Hualuoya Herb Bottle Label</title>
<link rel="stylesheet" href="https://fonts.googleapis.com/css2?family=Cinzel:wght@500&family=Montserrat:wght@600;700&display=swap">
<style>
  :root {
    --page-bg: #e8e8e8;
    --label-blue: #1d3a91;
    --label-blue-deep: #142c78;
    --mountain-mid: #2a4aa6;
    --mountain-dark: #0f2466;
    --seal-red: #d0161e;
    --stripe-red: #d81920;
    --gold: #e6b21f;
    --white: #ffffff;
  }
  * { margin: 0; padding: 0; box-sizing: border-box; }
  html, body {
    width: 1200px;
    height: 1200px;
    overflow: hidden;
    background: var(--page-bg);
  }
  .label {
    position: absolute;
    left: 100px;
    top: 200px;
    width: 1000px;
    height: 800px;
    overflow: hidden;
    background: linear-gradient(180deg, var(--label-blue) 0%, var(--label-blue-deep) 100%);
  }
  .label__mountains {
    position: absolute;
    left: 0;
    right: 0;
    bottom: 0;
    height: 470px;
    background:
      linear-gradient(180deg, rgba(42,74,166,0) 0%, rgba(42,74,166,0.45) 30%, rgba(20,44,120,0.6) 55%, var(--mountain-dark) 100%);
  }
  .label__stripe {
    position: absolute;
    left: 0;
    right: 0;
    height: 28px;
    background: var(--stripe-red);
  }
  .label__stripe--upper { top: 152px; }
  .label__stripe--lower { top: 199px; }
  .label__seal {
    position: absolute;
    left: 406px;
    top: 57px;
    width: 160px;
    height: 312px;
    background: var(--seal-red);
    display: flex;
    align-items: center;
    justify-content: center;
  }
  .label__seal::after {
    content: "";
    position: absolute;
    inset: 8px;
    border: 2px solid rgba(255,255,255,0.85);
  }
  .label__seal-name {
    writing-mode: vertical-rl;
    font-family: "Cinzel", serif;
    font-weight: 500;
    font-size: 40px;
    letter-spacing: 6px;
    color: var(--white);
  }
  .label__title {
    position: absolute;
    left: 0;
    right: 0;
    top: 478px;
    text-align: center;
    font-family: "Cinzel", serif;
    font-weight: 500;
    font-size: 70px;
    letter-spacing: 3px;
    color: var(--gold);
    line-height: 1;
  }
  .label__subtitle {
    position: absolute;
    left: 0;
    right: 0;
    top: 565px;
    text-align: center;
    font-family: "Montserrat", sans-serif;
    font-weight: 600;
    font-size: 31px;
    color: var(--gold);
  }
  .label__net {
    position: absolute;
    left: 406px;
    top: 715px;
    font-family: "Montserrat", sans-serif;
    font-weight: 700;
    font-size: 32px;
    color: var(--white);
  }
  .label__mark {
    position: absolute;
    left: 620px;
    top: 706px;
    display: flex;
    align-items: center;
    gap: 12px;
  }
  .label__mark-dot {
    width: 54px;
    height: 54px;
    border-radius: 50%;
    background: var(--seal-red);
  }
  .label__mark-name {
    font-family: "Montserrat", sans-serif;
    font-weight: 700;
    font-size: 22px;
    color: var(--white);
  }
</style>
</head>
<body>
  <main class="label">
    <div class="label__mountains" role="img" aria-label="Misty blue mountain range painted in layered ink washes"></div>
    <div class="label__stripe label__stripe--upper"></div>
    <div class="label__stripe label__stripe--lower"></div>
    <div class="label__seal"><span class="label__seal-name">Hualuoya</span></div>
    <h1 class="label__title">HUALUOYA</h1>
    <p class="label__subtitle">Concentrated Chinese Herbs</p>
    <p class="label__net">100g NET</p>
    <div class="label__mark">
      <span class="label__mark-dot"></span>
      <span class="label__mark-name">Hualuoya</span>
    </div>
  </main>
</body>
</html>
```